International Clinical Software Company needs a new business card design

We are looking for a new business card design for our company that has recently expanded into the UK market, making us a multinational company.
After having rebranded our website and produced a new style guide, we are looking for a business card that is creative and attention grabbing, while being consistent with the style and colour scheme used on the new website, www.brookvale.example
We produce care management technology for the aged care market, but the main aspect we aim to communicate is the human element of our software, and the way it assists in providing better care for aged people, and stronger relationships between aged people and the staff that care for them.
Our current business card is a dark green with gold text, which makes the text quite difficult to read, not very aesthetically appealing and the colour scheme looks quite dated.
We would like something fresh and modern, that can still be colourful but doesn't use large blocks of dark colour, and uses the colours within our logo.
Something tying in with the leaves that are used in our logo could work quite nicely, along with the Autumn/Fall colours of soft greens, yellows and reds (also in our existing logo). However also happy to look at fresh, completely out of the box ideas we may not have yet considered.
Target Market(s)
The people that receive this business card work in the aged card or health industry and are either corporate/management level staff or clinical (Registered Nurses, care workers etc.)
Industry/Entity Type
Health Product
Contact Information for Business Card
Company Name - BrookvaleTech
Company locations: United Kingdom, Australia, New Zealand
Staff Details:
Staff name: Dermot Quill
Staff job title: Executive Chairman
Staff email: d.quill@brookvale.example
Office phone number: 01632 960418
Font styles to use
Other font styles liked:
- Calibri
Requirements
Must have
- Must include the BrookvaleTech brand name in it's current font
- Must include logo (3 leaves in gold circle)
- Must include Business Card Details
Nice to have
- Elements of gold
- White space
- Something autumn themed but not too cliched
Should not have
- No blue - used by a major competitor and we would like to differentiate from them
- Large blocks of dark green colour (the green that appears in our leaves on the logo on our current business card is the background colour and it is far too dark)

```html
<!DOCTYPE html>
<html lang="en">
<head>
<meta charset="utf-8">
<title>BrookvaleTech — Business Card</title>
<link rel="stylesheet" href="https://fonts.googleapis.com/css2?family=Carlito:wght@400;700&display=swap">
<style>
  :root {
    --page-bg: #e6e6e4;
    --card-gold: #a08a62;
    --card-berry: #9b0138;
    --seal-white: #f3f2ef;
    --ring-gold: #a8916a;
    --name-red: #9e0a3c;
    --text-white: #ffffff;
    --wordmark: #9a865f;
  }
  * { box-sizing: border-box; margin: 0; padding: 0; }
  html, body {
    width: 1105px;
    height: 1200px;
    overflow: hidden;
    background: var(--page-bg);
    font-family: "Carlito", "Calibri", sans-serif;
  }
  .business-card {
    position: absolute;
    left: 72px;
    top: 325px;
    width: 960px;
    height: 549px;
    background: var(--card-gold);
    overflow: hidden;
  }
  .card-shapes {
    position: absolute;
    inset: 0;
  }
  .contact-block {
    position: absolute;
    left: 66px;
    top: 118px;
    color: var(--text-white);
  }
  .staff-name {
    font-weight: 700;
    font-size: 32px;
    letter-spacing: 0.5px;
    color: var(--name-red);
    line-height: 1;
    text-transform: uppercase;
  }
  .staff-title {
    font-size: 26px;
    line-height: 1;
    margin-top: 8px;
  }
  .locations {
    list-style: none;
    margin-top: 28px;
    font-size: 26px;
    line-height: 35px;
  }
  .contact-lines {
    list-style: none;
    margin-top: 22px;
    font-size: 26px;
    line-height: 37px;
  }
  .contact-lines li {
    display: flex;
    align-items: center;
  }
  .contact-icon {
    width: 22px;
    height: 22px;
    margin-right: 18px;
    flex: none;
  }
  .brand-name {
    position: absolute;
    left: 665px;
    top: 280px;
    transform: translateX(-50%);
    font-size: 60px;
    font-weight: 400;
    color: var(--wordmark);
    white-space: nowrap;
    line-height: 1;
  }
</style>
</head>
<body>
  <div class="business-card">
    <svg class="card-shapes" width="960" height="549" viewBox="0 0 960 549" aria-hidden="true">
      <rect class="berry-band" x="700" y="0" width="260" height="549" fill="var(--card-berry)"/>
      <circle class="seal-halo" cx="665" cy="276" r="280" fill="var(--seal-white)"/>
      <circle class="seal-ring" cx="665" cy="276" r="272" fill="none" stroke="var(--ring-gold)" stroke-width="3"/>
      <circle class="brand-dot" cx="665" cy="204" r="56" fill="none" stroke="var(--ring-gold)" stroke-width="4"/>
    </svg>

    <div class="contact-block">
      <h1 class="staff-name">Dermot Quill</h1>
      <p class="staff-title">Executive Chairman</p>
      <ul class="locations">
        <li>United Kingdom</li>
        <li>Australia</li>
        <li>New Zealand</li>
      </ul>
      <ul class="contact-lines">
        <li>
          <svg class="contact-icon" viewBox="0 0 24 24" aria-hidden="true">
            <path d="M6.6 10.8c1.4 2.8 3.8 5.1 6.6 6.6l2.2-2.2c.3-.3.7-.4 1-.2 1.1.4 2.3.6 3.6.6.6 0 1 .4 1 1V20c0 .6-.4 1-1 1C10.6 21 3 13.4 3 4c0-.6.4-1 1-1h3.5c.6 0 1 .4 1 1 0 1.3.2 2.5.6 3.6.1.3 0 .7-.2 1L6.6 10.8z" fill="var(--name-red)"/>
          </svg>
          <span>01632 960418</span>
        </li>
        <li>
          <svg class="contact-icon" viewBox="0 0 24 24" aria-hidden="true">
            <rect x="2" y="5" width="20" height="14" rx="1" fill="var(--name-red)"/>
            <path d="M3 6l9 7 9-7" fill="none" stroke="var(--card-gold)" stroke-width="1.8"/>
          </svg>
          <span>d.quill@brookvale.example</span>
        </li>
        <li>
          <svg class="contact-icon" viewBox="0 0 24 24" aria-hidden="true">
            <circle cx="12" cy="12" r="10" fill="var(--name-red)"/>
            <ellipse cx="12" cy="12" rx="4" ry="10" fill="none" stroke="var(--card-gold)" stroke-width="1.5"/>
            <line x1="2" y1="12" x2="22" y2="12" stroke="var(--card-gold)" stroke-width="1.5"/>
          </svg>
          <span>www.brookvale.example</span>
        </li>
      </ul>
    </div>

    <p class="brand-name">BrookvaleTech</p>
  </div>
</body>
</html>
```